Core values in our company OTK (Oversight and Transit Keepers)

Do good:
1. Being Direct and communicative for the benefit of all parties
2. Working for the Benefit of the company, client and team members
3. Wanting to improve to create a better impact
4. Having healthy rivalry
Be ahead of curve:
1. Having the confidence to break through barriers which arise
2. Desire to grow and learn towards establishment and agreed goal
3. Getting off the sidelines and get into the game
4. Keeping the end game in mind having due regard to processes and milestones
5. Self starter and works on own initiative
6. Diligent and impactful in your field of responsibility
Truth and Honesty
2. Have the confidence and ability to speak what you really want to communicate
3. Being truthful to yourself, clients and colleagues to find the innovations that lie within
4. Seeking the truth by opening things up for discussion
5. Being Optimistic
Background Information on our Company:OTK is a professional law firm in London Docklands. We caters for both private and corporate clients ranging from highly regarded and established law firms to boutique and niche immigration practices. We also specialises in expert legal advice and prides itself on providing services that go beyond the expectations of its clients.
What we need: We need a Poster about Truth and Honesty, this is to show one of our values as a company. It will need to be vibrant and straight to the point. Colours can be orange grey white and yellow. Attached is our company logo.
Reason: To remind colleagues that this is one of our main values and it is instilled in our company.
Things we would like:
1. To create a point of focus
2. Use shapes to create visual interest
3. Use creative illustrations
4. Take the viewer’s focus on a journey with clever perspective
Industry/Entity Type
Legal
Requirements
Must have
- a globe (Picture)
- Do good:
- 1. Being Direct and communicative for the benefit of all parties
- 2. Working for the Benefit of the company, client and team members
- 3. Wanting to improve to create a better impact
- 4. Having healthy rivalry
- Be ahead of curve:
- 1. Having the confidence to break through barriers which arise
- 2. Desire to grow and learn towards establishment and agreed goal
- 3. Getting off the sidelines and get into the game
- 4. Keeping the end game in mind having due regard to processes and milestones
- 5. Self starter and works on own initiative
- 6. Diligent and impactful in your field of responsibility
- Truth and Honesty
- 2. Have the confidence and ability to speak what you really want to communicate
- 3. Being truthful to yourself, clients and colleagues to find the innovations that lie within
- 4. Seeking the truth by opening things up for discussion
- 5. Being Optimistic

```html
<!DOCTYPE html>
<html lang="en">
<head>
<meta charset="utf-8">
<title>Core Values in OTK</title>
<link href="https://fonts.googleapis.com/css2?family=Montserrat:wght@500;600;700&family=Merriweather:wght@700&display=swap" rel="stylesheet">
<style>
  :root{
    --page-bg:#e4e4e4;
    --ink:#3a3a3a;
    --ink-soft:#4a4a4a;
    --orange:#f07a10;
    --yellow:#ffc21a;
    --navy-deep:#0b1a45;
    --navy:#183a86;
    --white:#ffffff;
    --footer-dark:#3b3b3b;
  }
  *{margin:0;padding:0;box-sizing:border-box}
  html,body{width:1200px;height:2163px;overflow:hidden;background:var(--page-bg)}
  .poster{position:absolute;left:40px;top:291px;width:1120px;height:1581px;background:var(--white);overflow:hidden;
    font-family:"Montserrat",sans-serif;color:var(--ink);box-shadow:0 6px 30px rgba(0,0,0,.18)}
  .header{position:absolute;left:0;top:0;width:100%;height:155px;
    background:linear-gradient(180deg,#f4f4f4,#d9d9d9)}
  .brand-panel{position:absolute;left:0;top:0;width:430px;height:155px;background:var(--white);
    border-bottom-right-radius:80px 155px;box-shadow:4px 0 10px rgba(0,0,0,.12)}
  .brand{position:absolute;left:70px;top:30px;display:flex;align-items:center;gap:14px}
  .brand-mark{width:26px;height:26px;background:var(--orange)}
  .brand-name{font-size:58px;font-weight:700;color:var(--ink);letter-spacing:1px;line-height:1}
  .brand-sub{position:absolute;left:70px;top:102px;font-size:19px;font-weight:600;color:var(--ink)}
  .title{position:absolute;right:45px;top:48px;font-size:60px;font-weight:700;color:var(--ink);letter-spacing:.5px}
  .globe{position:absolute;left:0;top:155px;width:100%;height:522px;
    background:radial-gradient(ellipse at 58% 60%,var(--navy) 0%,#10296a 45%,var(--navy-deep) 100%)}
  .left-panel{position:absolute;left:0;top:677px;width:520px;height:795px;
    background:linear-gradient(90deg,#ececec,#f7f7f7);border-bottom-right-radius:140px 320px;
    box-shadow:6px 0 14px rgba(0,0,0,.12)}
  .right-panel{position:absolute;left:486px;top:677px;right:0;height:795px;background:var(--white);
    border-top-left-radius:60px 40px}
  .intro{position:absolute;left:38px;top:730px;width:420px;font-size:18.5px;line-height:1.22;
    text-align:justify;font-weight:500;color:var(--ink-soft)}
  .intro p+p{margin-top:16px}
  .pill{position:absolute;height:66px;border-radius:0 33px 33px 0;
    background:linear-gradient(90deg,var(--orange),var(--yellow));
    font-family:"Merriweather",serif;font-size:25px;font-weight:700;color:var(--ink);
    display:flex;align-items:center;padding-left:36px;box-shadow:0 3px 6px rgba(0,0,0,.15)}
  .pill-truth{left:0;top:1030px;width:356px;padding-left:30px}
  .pill-good{left:486px;top:710px;width:356px}
  .pill-curve{left:486px;top:1040px;width:356px}
  .values{position:absolute;list-style:none}
  .values li{display:flex;gap:14px;font-size:19px;font-weight:700;line-height:1.1;color:var(--ink)}
  .values li svg{flex:none;width:20px;height:20px;margin-top:1px}
  .values-truth{left:68px;top:1132px;width:405px}
  .values-truth li{margin-bottom:20px}
  .values-good{left:500px;top:806px;width:590px}
  .values-good li{margin-bottom:20px}
  .values-curve{left:500px;top:1134px;width:600px}
  .values-curve li{margin-bottom:22px}
  .footer{position:absolute;left:0;bottom:0;width:100%;height:109px;
    background:linear-gradient(90deg,var(--orange) 0%,#8a4f1f 28%,var(--footer-dark) 55%,var(--footer-dark) 100%);
    display:flex;align-items:center;justify-content:flex-end;padding-right:30px;gap:20px;color:var(--white);
    font-size:33px;font-weight:700}
  .contact{display:flex;align-items:center;gap:10px}
  .divider{width:2px;height:46px;background:rgba(255,255,255,.6)}
</style>
</head>
<body>
<div class="poster">
  <header class="header">
    <div class="brand-panel">
      <div class="brand"><span class="brand-mark"></span><span class="brand-name">OTK</span></div>
      <div class="brand-sub">Oversight and Transit Keepers</div>
    </div>
    <h1 class="title">CORE VALUES IN OTK</h1>
  </header>

  <div class="globe" role="img" aria-label="Dotted blue globe with glowing travel routes connecting cities around the world"></div>

  <div class="left-panel"></div>
  <div class="right-panel"></div>

  <div class="intro">
    <p>OTK is a professional law firm in London Docklands. We caters for both private and corporate clients ranging from highly regarded and established law firms to boutique and niche immigration practices.</p>
    <p>We also specialises in expert legal advice and prides itself on providing services that go beyond the expectations of its clients.</p>
  </div>

  <div class="pill pill-truth">Truth and Honesty</div>
  <ul class="values values-truth">
    <li><svg viewBox="0 0 20 20"><circle cx="10" cy="10" r="8" fill="none" stroke="#f07a10" stroke-width="2"/><path d="M6 10l3 3 5-6" fill="none" stroke="#f07a10" stroke-width="2"/></svg><span>Having the confidence to break through barriers which arise</span></li>
    <li><svg viewBox="0 0 20 20"><circle cx="10" cy="10" r="8" fill="none" stroke="#f07a10" stroke-width="2"/><path d="M6 10l3 3 5-6" fill="none" stroke="#f07a10" stroke-width="2"/></svg><span>Have the confidence and ability to speak what you really want to communicate</span></li>
    <li><svg viewBox="0 0 20 20"><circle cx="10" cy="10" r="8" fill="none" stroke="#f07a10" stroke-width="2"/><path d="M6 10l3 3 5-6" fill="none" stroke="#f07a10" stroke-width="2"/></svg><span>Being truthful to yourself, clients and colleagues to find the innovations that lie within</span></li>
    <li><svg viewBox="0 0 20 20"><circle cx="10" cy="10" r="8" fill="none" stroke="#f07a10" stroke-width="2"/><path d="M6 10l3 3 5-6" fill="none" stroke="#f07a10" stroke-width="2"/></svg><span>Seeking the truth by opening things up for discussion</span></li>
    <li><svg viewBox="0 0 20 20"><circle cx="10" cy="10" r="8" fill="none" stroke="#f07a10" stroke-width="2"/><path d="M6 10l3 3 5-6" fill="none" stroke="#f07a10" stroke-width="2"/></svg><span>Being Optimistic</span></li>
  </ul>

  <div class="pill pill-good">Do good:</div>
  <ul class="values values-good">
    <li><svg viewBox="0 0 20 20"><circle cx="10" cy="10" r="8" fill="none" stroke="#f07a10" stroke-width="2"/><path d="M6 10l3 3 5-6" fill="none" stroke="#f07a10" stroke-width="2"/></svg><span>Being Direct and communicative for the<br>benefit of all parties</span></li>
    <li><svg viewBox="0 0 20 20"><circle cx="10" cy="10" r="8" fill="none" stroke="#f07a10" stroke-width="2"/><path d="M6 10l3 3 5-6" fill="none" stroke="#f07a10" stroke-width="2"/></svg><span>Working for the Benefit of the company, client<br>and team members</span></li>
    <li><svg viewBox="0 0 20 20"><circle cx="10" cy="10" r="8" fill="none" stroke="#f07a10" stroke-width="2"/><path d="M6 10l3 3 5-6" fill="none" stroke="#f07a10" stroke-width="2"/></svg><span>Wanting to improve to create a better impact</span></li>
    <li><svg viewBox="0 0 20 20"><circle cx="10" cy="10" r="8" fill="none" stroke="#f07a10" stroke-width="2"/><path d="M6 10l3 3 5-6" fill="none" stroke="#f07a10" stroke-width="2"/></svg><span>Having healthy rivalry</span></li>
  </ul>

  <div class="pill pill-curve">Be ahead of curve:</div>
  <ul class="values values-curve">
    <li><svg viewBox="0 0 20 20"><circle cx="10" cy="10" r="8" fill="none" stroke="#f07a10" stroke-width="2"/><path d="M6 10l3 3 5-6" fill="none" stroke="#f07a10" stroke-width="2"/></svg><span>Having the confidence to break through<br>barriers which arise</span></li>
    <li><svg viewBox="0 0 20 20"><circle cx="10" cy="10" r="8" fill="none" stroke="#f07a10" stroke-width="2"/><path d="M6 10l3 3 5-6" fill="none" stroke="#f07a10" stroke-width="2"/></svg><span>Desire to grow and learn towards establishment<br>and agreed goal</span></li>
    <li><svg viewBox="0 0 20 20"><circle cx="10" cy="10" r="8" fill="none" stroke="#f07a10" stroke-width="2"/><path d="M6 10l3 3 5-6" fill="none" stroke="#f07a10" stroke-width="2"/></svg><span>Getting off the sidelines and get into the game</span></li>
    <li><svg viewBox="0 0 20 20"><circle cx="10" cy="10" r="8" fill="none" stroke="#f07a10" stroke-width="2"/><path d="M6 10l3 3 5-6" fill="none" stroke="#f07a10" stroke-width="2"/></svg><span>Keeping the end game in mind having due<br>regard to processes and milestones</span></li>
    <li><svg viewBox="0 0 20 20"><circle cx="10" cy="10" r="8" fill="none" stroke="#f07a10" stroke-width="2"/><path d="M6 10l3 3 5-6" fill="none" stroke="#f07a10" stroke-width="2"/></svg><span>Self starter and works on own initiative</span></li>
    <li><svg viewBox="0 0 20 20"><circle cx="10" cy="10" r="8" fill="none" stroke="#f07a10" stroke-width="2"/><path d="M6 10l3 3 5-6" fill="none" stroke="#f07a10" stroke-width="2"/></svg><span>Diligent and impactful in your field of responsibility</span></li>
  </ul>

  <footer class="footer">
    <span class="contact">
      <svg width="32" height="32" viewBox="0 0 32 32"><rect x="1" y="1" width="30" height="30" rx="6" fill="#fff"/><path d="M11 7c1 0 2 3 2.5 4.5.3 1-1.5 2-1.5 2.5 0 1.5 4 5.5 5.5 5.5.5 0 1.5-1.8 2.5-1.5C21.5 18.5 25 19.5 25 21c0 1.5-2 4-4 4C14 25 7 18 7 11c0-2 2.5-4 4-4z" fill="#3b3b3b"/></svg>
      +44 2071 5538
    </span>
    <span class="divider"></span>
    <span class="contact">
      <svg width="28" height="28" viewBox="0 0 28 28" fill="none" stroke="#fff" stroke-width="2"><circle cx="14" cy="14" r="12"/><ellipse cx="14" cy="14" rx="5" ry="12"/><path d="M2 14h24M4 8h20M4 20h20"/></svg>
      www.otk-keepers.com
    </span>
  </footer>
</div>
</body>
</html>
```